Brackwater Vale Medical Website to make connecting and communicating easier

To create a unique, user-friendly, professional website for patients and professionals to access education/ information, forms, appointments, contact details, and data about us, and for us to have the capacity to link to various cloud-based platforms.
To use the logo design and colour scheme we have just sourced.

WEBSITE to be eye catching, Inspiring and alluring
- efficient and logical
- professional and trustworthy appearance
- health focus "living health matters"
- user friendly
- ability to link with cloud-based software and video conferencing tools/ telehealth
- colours- black/ white teal and ?silver

PAGES:
page 1 - Our clinic and staff, services offered, contact us- address/ map / contact details- social media connections
page 2- patients and visitors - New patient forms to complete, news and patient informtion (educatinal)
page 3 - health professionals -referral forms, research and education
page 3- online appointments
page 4 - Quick links - partners, other services
page 5- privacy policy, disclaimer

Need extra days to review

HI, Could we please extend the deadline another 5 days, so sorry just struggling with my workload to be able to keep up and I am wanting to liaise more with the designer that I will choose. I am so happy with PixelForge and all the designers - thank you! Thank you so much!!

Target Market(s)

Patients - mostly over 60's so the website must be minimal clicks and simple to navigate
Professionals - for education and access forms

Industry/Entity Type

Health Care

Coding

Coded - Design and coding required

Number of Pages Required

5+ page

Font styles to use
Sans Serif
Script

Colors
33b8a4
86cfc6

Requirements
Must have
• WEBSITE to be eye catching, Inspiring and alluring
- efficient and logical
- user friendly

WEBSITE - professional and user friendly
- ability to link with cloud based software and videoconferencing/ telehealth
Nice to have
• clean and crisp presentation
happy for an innovative look
room to add more services and ability to link pages and resources
Should not have
• Please ensure the website is not:
clunky
difficult to navigate
common and cheap looking

```html
<!DOCTYPE html>
<html lang="en">
<head>
<meta charset="utf-8">
<title>Brackwater Vale Medical</title>
<link rel="stylesheet" href="https://fonts.googleapis.com/css2?family=Rajdhani:wght@500;600;700&family=Roboto:wght@400;500&display=swap">
<style>
:root{
  --teal:#1fb29f;
  --teal-soft:#86cfc6;
  --black:#000;
  --dark:#333;
  --ink:#444;
  --muted:#6a6a6a;
  --white:#fff;
  --line:#d9d9d9;
}
*{box-sizing:border-box;margin:0;padding:0}
html,body{width:1200px;height:3750px;overflow:hidden;background:var(--white)}
body{position:relative;font-family:"Roboto",Arial,sans-serif;color:var(--ink)}
.head-font{font-family:"Rajdhani","Roboto",sans-serif}
section,header,footer{position:absolute;left:0;width:1200px}

/* header */
.site-header{top:0;height:141px;background:var(--black);color:var(--white)}
.brand{position:absolute;left:172px;top:40px;display:flex;align-items:center;gap:10px}
.brand-dot{width:30px;height:30px;border-radius:50%;background:var(--teal)}
.brand-name{font-family:"Rajdhani",sans-serif;font-weight:600;font-size:20px;line-height:1.05;color:var(--teal);width:120px}
.top-contact{position:absolute;top:30px;display:flex;align-items:center;gap:10px;font-size:12px;font-weight:500;line-height:1.35}
.icon-ring{width:34px;height:34px;border:2px solid var(--teal);border-radius:50%;display:flex;align-items:center;justify-content:center}
.main-nav{position:absolute;top:99px;left:373px;display:flex;gap:0;font-family:"Rajdhani",sans-serif;font-weight:700;font-size:13.5px;letter-spacing:.3px}
.main-nav a{color:var(--white);text-decoration:none;margin-right:30px}
.main-nav a.active{color:var(--teal)}

/* hero */
.hero{top:141px;height:561px}
.hero-photo{position:absolute;inset:0;background:linear-gradient(180deg,#7d93a3 0%,#5d7788 40%,#3e5669 70%,#514436 100%)}
.hero-title{position:absolute;left:677px;top:175px;font-family:"Rajdhani",sans-serif;font-weight:700;font-size:63px;line-height:.93;color:var(--white)}
.btn{display:inline-block;background:var(--teal);color:var(--white);font-family:"Rajdhani",sans-serif;font-weight:700;text-decoration:none;text-align:center}
.hero-btn{position:absolute;left:680px;top:309px;width:269px;height:51px;line-height:51px;border-radius:26px;font-size:19px}

/* section headings */
.section-title{position:absolute;left:0;width:1200px;text-align:center;font-family:"Rajdhani",sans-serif;font-weight:700;font-size:40px;color:var(--dark)}
.divider{position:absolute;left:489px;width:224px;height:10px}
.divider::before,.divider::after{content:"";position:absolute;top:4px;width:96px;height:2px;background:var(--teal)}
.divider::before{left:0}.divider::after{right:0}
.divider span{position:absolute;left:107px;top:1px;width:8px;height:8px;border-radius:50%;background:var(--teal)}

/* services */
.services{top:702px;height:627px}
.service-card{position:absolute;top:205px;width:206px;height:313px;background:var(--white);box-shadow:0 0 8px rgba(31,178,159,.35);text-align:center;padding-top:27px}
.service-icon{width:99px;height:99px;border-radius:50%;background:var(--teal);margin:0 auto;display:flex;align-items:center;justify-content:center}
.service-name{font-family:"Rajdhani",sans-serif;font-weight:700;font-size:19px;color:var(--dark);margin-top:22px}
.service-text{font-size:13px;line-height:1.25;color:var(--muted);margin:16px auto 0;width:168px}

/* about */
.about{top:1329px;height:532px;background:linear-gradient(90deg,#1fb29f 0%,#22b5a2 65%,#3cbcaa 100%)}
.about-title{position:absolute;left:154px;top:94px;font-family:"Rajdhani",sans-serif;font-weight:700;font-size:41px;line-height:1.32;color:var(--white)}
.about-text{position:absolute;left:154px;top:203px;width:385px;font-size:12.5px;line-height:1.27;color:var(--white)}
.about-badge{position:absolute;left:647px;top:146px;width:288px;height:288px;border-radius:50%;background:#262626;display:flex;align-items:center;justify-content:center;gap:12px}
.about-badge .brand-name{font-size:30px;width:150px}

/* clinic */
.clinic{top:1861px;height:728px;background:var(--dark);color:var(--white)}
.clinic .section-title{color:var(--white);top:55px}
.clinic-text{position:absolute;left:305px;top:155px;width:590px;text-align:center;font-size:13px;line-height:1.25}
.clinic-btn{position:absolute;left:526px;top:257px;width:148px;height:44px;line-height:44px;border-radius:22px;font-size:14px}
.staff-photo{position:absolute;left:80px;top:337px;width:1080px;height:391px;background:linear-gradient(180deg,#4a4a4a 0%,#8a9bb0 35%,#b9c6d6 70%,#c7d1de 100%)}

/* contact */
.contact{top:2589px;height:818px}
.contact-item{position:absolute;top:188px;width:230px;text-align:center;font-family:"Rajdhani",sans-serif;font-weight:700;font-size:15px;line-height:1.35;color:var(--dark)}
.contact-item .icon-ring{margin:0 auto 19px;width:36px;height:36px}
.contact-form{position:absolute;left:154px;top:345px;width:407px;height:339px;background:var(--white);box-shadow:0 0 6px rgba(0,0,0,.12);padding:28px 30px 0}
.field{height:52px;border-bottom:1px solid var(--line);font-size:12.5px;color:var(--muted);padding-top:11px;margin-right:0;width:348px}
.field.message{height:92px}
.form-btn{position:absolute;left:30px;top:275px;width:108px;height:38px;line-height:38px;border-radius:19px;font-size:16px}
.map{position:absolute;left:588px;top:345px;width:459px;height:342px;background:linear-gradient(135deg,#dfe8d6 0%,#eef0ea 45%,#e4ebdb 100%)}

/* footer */
.site-footer{top:3407px;height:343px;background:var(--black);color:var(--white)}
.footer-brand{position:absolute;left:520px;top:118px;display:flex;align-items:center;gap:10px}
.social{position:absolute;left:495px;top:215px;display:flex;gap:30px}
.social span{width:30px;height:30px;border-radius:50%;background:var(--teal)}
.copyright{position:absolute;left:0;width:1200px;top:266px;text-align:center;font-size:13px}
.copyright a{color:var(--teal);margin-left:6px}

.zigzags{position:absolute;left:0;top:0;width:1200px;height:3750px;pointer-events:none}
</style>
</head>
<body>

<header class="site-header">
  <div class="brand"><span class="brand-dot"></span><span class="brand-name">Brackwater Vale Medical</span></div>
  <div class="top-contact" style="left:659px">
    <span class="icon-ring"><svg width="16" height="12" viewBox="0 0 16 12"><rect x="0.5" y="0.5" width="15" height="11" rx="1" fill="none" stroke="#1fb29f"/><path d="M1 1l7 6 7-6" fill="none" stroke="#1fb29f"/></svg></span>
    <span>Email:<br>hello@brackwatervale.com</span>
  </div>
  <div class="top-contact" style="left:889px">
    <span class="icon-ring"><svg width="16" height="16" viewBox="0 0 24 24"><path d="M6.6 10.8a15 15 0 006.6 6.6l2.2-2.2c.3-.3.7-.4 1-.2 1.1.4 2.3.6 3.6.6.6 0 1 .4 1 1V20c0 .6-.4 1-1 1A17 17 0 013 4c0-.6.4-1 1-1h3.5c.6 0 1 .4 1 1 0 1.3.2 2.5.6 3.6.1.3 0 .7-.2 1z" fill="#1fb29f"/></svg></span>
    <span>Phone:<br>125-000-4470</span>
  </div>
  <nav class="main-nav">
    <a class="active" href="#">HOME</a>
    <a href="#">PATIENTS AND VISITORS</a>
    <a href="#">HEALTH PROFESSIONALS</a>
    <a href="#">ONLINE APPOINTMENTS</a>
    <a href="#">QUICK LINKS</a>
  </nav>
</header>

<section class="hero">
  <div class="hero-photo" role="img" aria-label="Photo of a smiling older couple throwing autumn leaves on a lakeside jetty"></div>
  <h1 class="hero-title">LIVING HEALTH<br>MATTERS</h1>
  <a class="btn hero-btn" href="#">ONLINE APPOINTMENTS</a>
</section>

<section class="services">
  <h2 class="section-title" style="top:109px">SERVICES OFFERED</h2>
  <div class="divider" style="top:168px"><span></span></div>

  <article class="service-card" style="left:154px">
    <div class="service-icon"><svg width="46" height="46" viewBox="0 0 46 46"><circle cx="23" cy="23" r="20" fill="none" stroke="#fff" stroke-width="3"/><path d="M23 12v22M12 23h22" stroke="#fff" stroke-width="7"/></svg></div>
    <h3 class="service-name">Service Name</h3>
    <p class="service-text">At vero eos et accusamus et iusto odio dignissimos ducimus qui blanditiis prae sentium voluptatum dele niti atque corruptio.</p>
  </article>
  <article class="service-card" style="left:382px">
    <div class="service-icon"><svg width="50" height="44" viewBox="0 0 50 44"><path d="M25 42L5 22A12 12 0 0125 8a12 12 0 0120 14z" fill="#fff"/><path d="M8 22h10l3-6 4 12 3-6h14" fill="none" stroke="#1fb29f" stroke-width="2.5"/></svg></div>
    <h3 class="service-name">Service Name</h3>
    <p class="service-text">At vero eos et accusamus et iusto odio dignissimos ducimus qui blanditiis prae sentium voluptatum dele niti atque corruptio.</p>
  </article>
  <article class="service-card" style="left:611px">
    <div class="service-icon"><svg width="36" height="46" viewBox="0 0 36 46"><rect x="2" y="5" width="32" height="39" rx="3" fill="#fff"/><rect x="11" y="1" width="14" height="8" rx="2" fill="#fff" stroke="#1fb29f" stroke-width="2"/><path d="M18 14v8M14 18h8M9 28h18M9 33h18M9 38h18" stroke="#1fb29f" stroke-width="2.5"/></svg></div>
    <h3 class="service-name">Service Name</h3>
    <p class="service-text">At vero eos et accusamus et iusto odio dignissimos ducimus qui blanditiis prae sentium voluptatum dele niti atque corruptio.</p>
  </article>
  <article class="service-card" style="left:840px">
    <div class="service-icon"><svg width="40" height="46" viewBox="0 0 40 46"><path d="M20 2l17 6v13c0 11-8 19-17 23C11 40 3 32 3 21V8z" fill="#fff"/><circle cx="20" cy="22" r="8" fill="#1fb29f"/><path d="M20 17v10M15 22h10" stroke="#fff" stroke-width="3"/></svg></div>
    <h3 class="service-name">Service Name</h3>
    <p class="service-text">At vero eos et accusamus et iusto odio dignissimos ducimus qui blanditiis prae sentium voluptatum dele niti atque corruptio.</p>
  </article>
</section>

<section class="about">
  <h2 class="about-title">ABOUT BRACKWATER<br>VALE MEDICAL</h2>
  <p class="about-text">At vero eos et accusamus et iusto odio dignissimos ducimus qui blanditiis praesentium voluptatum deleniti atque corrupti quosd olores et quas olestias excepturi sint occaecati cupiditate nonpr ovident, similique sunt in culpa qui officia deserunt mollitia ani mi, id est laborum et dolorum fuga. Et harum quidem rerum fac ilis est et expdita distinctioam libro temporeo eos et accusam iusto odio dignissimos ducimus qui blanditiis praesentium lovo-luptatum deleniti atque corrupti quosdolores et quas olestias excepturi sint occaecati cupiditate nonpr ovident</p>
  <div class="about-badge"><span class="brand-name">Brackwater Vale Medical</span></div>
</section>

<section class="clinic">
  <h2 class="section-title">OUR CLINIC AND STAFF</h2>
  <div class="divider" style="top:115px"><span></span></div>
  <p class="clinic-text">At vero eos et accusamus et iusto odio dignissimos ducimus qui blanditiis praesentium voluptatu m deleniti atque corrupti quosdolores et quas olestias excepturi sint occaecati cupiditate nonpr ov ident, similique sunt in culpa qui officia deserunt mollitia animi, id est laborum et dolorum fuga. harum quidem rerum facilis est et expdita distinctioam libro temport vero eos et accusamus et iusto odio dignissimos ducimus qui blanditiis praesentium voluptatum deleniti.</p>
  <a class="btn clinic-btn" href="#">MEET OUR TEAM</a>
  <div class="staff-photo" role="img" aria-label="Group photo of smiling clinic doctors and nurses in white coats and blue scrubs"></div>
</section>

<section class="contact">
  <h2 class="section-title" style="top:90px">CONTACT US</h2>
  <div class="divider" style="top:149px"><span></span></div>

  <div class="contact-item" style="left:264px">
    <div class="icon-ring"><svg width="14" height="18" viewBox="0 0 14 18"><path d="M7 17S1 10 1 6.5a6 6 0 0112 0C13 10 7 17 7 17z" fill="none" stroke="#1fb29f" stroke-width="1.6"/><circle cx="7" cy="6.5" r="2" fill="#1fb29f"/></svg></div>
    7200 W. Ferngate Blvd, Suite 203<br>loe125 comyp Dummy lore
  </div>
  <div class="contact-item" style="left:507px">
    <div class="icon-ring" style="background:#fff"><svg width="20" height="20" viewBox="0 0 20 20"><circle cx="10" cy="10" r="9" fill="#1fb29f"/><rect x="5" y="6.5" width="10" height="7" fill="#fff"/><path d="M5 6.5l5 4 5-4" fill="none" stroke="#1fb29f"/></svg></div>
    Email us:<br>hello@brackwatervale.com
  </div>
  <div class="contact-item" style="left:693px">
    <div class="icon-ring"><svg width="16" height="16" viewBox="0 0 24 24"><path d="M6.6 10.8a15 15 0 006.6 6.6l2.2-2.2c.3-.3.7-.4 1-.2 1.1.4 2.3.6 3.6.6.6 0 1 .4 1 1V20c0 .6-.4 1-1 1A17 17 0 013 4c0-.6.4-1 1-1h3.5c.6 0 1 .4 1 1 0 1.3.2 2.5.6 3.6.1.3 0 .7-.2 1z" fill="#1fb29f"/></svg></div>
    Phone:<br>11000-526-4470
  </div>

  <form class="contact-form">
    <div class="field">Name:</div>
    <div class="field">Phone:</div>
    <div class="field">Email:</div>
    <div class="field message">Message:</div>
    <span class="btn form-btn">SUBMIT</span>
  </form>
  <div class="map" role="img" aria-label="Street map showing the clinic location"></div>
</section>

<footer class="site-footer">
  <div class="footer-brand"><span class="brand-dot"></span><span class="brand-name" style="font-size:22px;width:140px">Brackwater Vale Medical</span></div>
  <div class="social" aria-label="Social media links"><span></span><span></span><span></span><span></span></div>
  <p class="copyright">Copyright 2020 All Rights Reserved. <a href="#">Privacy policy</a> <a href="#">Disclaimer</a></p>
</footer>

<svg class="zigzags" viewBox="0 0 1200 3750" aria-hidden="true">
  <polygon points="466,702 550,795 578,702" fill="#4a5a5c"/>
  <polygon points="578,702 612,568 648,702" fill="#fff"/>
  <polygon points="800,1329 840,1410 869,1329" fill="#fff"/>
  <polygon points="903,1329 949,1449 975,1329" fill="#fff"/>
  <polygon points="869,1329 888,1242 903,1329" fill="#1fb29f"/>
  <polygon points="175,1861 211,1743 237,1861" fill="#333"/>
  <polygon points="237,1861 272,1951 298,1861" fill="#1fb29f"/>
  <polygon points="298,1861 320,1784 360,1861" fill="#333"/>
  <polygon points="852,3407 885,3541 916,3407" fill="#fff"/>
  <polygon points="973,3407 996,3494 1034,3407" fill="#fff"/>
  <polygon points="916,3407 946,3305 973,3407" fill="#000"/>
</svg>

</body>
</html>
```